Re-design a website for a millionaire mentor

We need an expert website designer to re-design the website qBrightvoyage.com

The website would have 4 pages. A home page, Summit Circle page, Book RM page and an About page.

Here are some reference websites

https://www.kdmotivates.example
https://dorvalenm.example/

I will also attach a beginning of mockup of the home page I did myself to give an idea of the style we like, please use the quote "If you are not chasing your potential you are wasting your life" instead of the one in the current website...

You don't have the use the mockup (just the quote) and are free to use all your creativity.

Target Market(s)

Entrepreneurs

Number of Pages Required

4 page

Font styles to use
Other font styles liked:
• Franklin Gothic

Requirements
Must have
• -Call of action on the main page to download a free business plan
• -Book rm page check out reference: http://www.bookdorianvale.example
• -summit circle page with a button to sign in or join the summit circle. Check out reference for example: https://www.kdmotivates.example/pulse_academy

```html
<!DOCTYPE html>
<html lang="en">
<head>
<meta charset="utf-8">
<title>Bright Voyage — Millionaire Mentor</title>
<link rel="stylesheet" href="https://fonts.googleapis.com/css2?family=Libre+Franklin:wght@700;800;900&family=Permanent+Marker&family=Montserrat:wght@500;600&display=swap">
<style>
  :root {
    --brand-red: #e83232;
    --ink: #111111;
    --white: #ffffff;
    --sky-top: #a3acba;
    --sky-mid: #5d6572;
    --city-dark: #2b2e35;
  }
  * { margin: 0; padding: 0; box-sizing: border-box; }
  html, body { width: 960px; height: 1200px; overflow: hidden; }
  body { font-family: "Libre Franklin", "Franklin Gothic Medium", Arial, sans-serif; background: var(--brand-red); color: var(--white); }

  .hero { position: relative; width: 960px; height: 544px; }
  .hero-photo {
    position: absolute; inset: 0;
    background: linear-gradient(180deg, var(--sky-top) 0%, #8b8f98 40%, var(--sky-mid) 62%, var(--city-dark) 100%);
  }
  .site-header {
    position: absolute; top: 16px; left: 32px; right: 32px;
    display: flex; justify-content: space-between; align-items: flex-start;
  }
  .brand {
    display: flex; align-items: center; gap: 8px; margin-top: 14px;
    font-weight: 800; font-size: 20px; color: var(--white); text-transform: uppercase; letter-spacing: 0.5px;
  }
  .brand-mark { width: 18px; height: 18px; background: var(--brand-red); }
  .main-nav { display: flex; gap: 47px; margin-top: 21px; }
  .main-nav a {
    font-weight: 800; font-size: 15px; color: var(--white); text-decoration: none; text-transform: uppercase;
  }
  .main-nav a.is-current { color: var(--brand-red); }

  .hero-title {
    position: absolute; left: 32px; top: 150px;
    font-family: "Permanent Marker", "Marker Felt", "Brush Script MT", fantasy;
    font-weight: 400; font-size: 35px; line-height: 44px; letter-spacing: 1px; font-style: normal;
  }
  .hero-title .accent { color: var(--brand-red); }
  .hero-intro {
    position: absolute; left: 32px; top: 218px; width: 385px;
    font-weight: 800; font-size: 14.5px; line-height: 19px; text-transform: uppercase;
  }
  .btn {
    display: flex; align-items: center; justify-content: center; gap: 8px;
    font-weight: 800; font-size: 13.5px; text-transform: uppercase; color: var(--white); text-decoration: none;
  }
  .btn-live {
    position: absolute; left: 148px; top: 314px; width: 198px; height: 40px;
    background: var(--ink); border: 2px solid var(--brand-red);
  }

  .video-section { position: relative; height: 656px; }
  .mentor-quote {
    position: absolute; left: 120px; right: 120px; top: 34px;
    text-align: center; font-weight: 800; font-size: 18px; line-height: 24px; text-transform: uppercase;
  }
  .video-player {
    position: absolute; left: 120px; top: 101px; width: 720px; height: 400px;
    background: linear-gradient(135deg, #6f6450 0%, #3e352a 35%, #2a2420 60%, #b9b3a6 85%, #8a857c 100%);
    font-family: "Montserrat", Arial, sans-serif;
  }
  .video-channel {
    position: absolute; left: 16px; top: 16px; display: flex; align-items: center; gap: 10px;
    font-weight: 600; font-size: 14px;
  }
  .video-avatar { width: 32px; height: 32px; border-radius: 50%; background: #777; }
  .video-actions { position: absolute; right: 32px; top: 15px; display: flex; gap: 26px; }
  .video-action { display: flex; flex-direction: column; align-items: center; gap: 8px; font-size: 12px; font-weight: 500; }
  .video-play {
    position: absolute; left: 320px; top: 172px; width: 80px; height: 56px; border-radius: 14px;
    background: var(--white); display: flex; align-items: center; justify-content: center;
  }
  .btn-cta {
    position: absolute; left: 380px; top: 534px; width: 200px; height: 40px;
    border: 2px solid var(--white); font-size: 12.5px;
  }
  .btn-plan {
    position: absolute; left: 350px; top: 594px; width: 260px; height: 40px;
    background: var(--ink); border: 2px solid var(--ink); font-size: 12.5px;
  }
</style>
</head>
<body>
  <section class="hero">
    <div class="hero-photo" role="img" aria-label="Photo of a man in a suit standing on a rooftop at dusk overlooking a city skyline"></div>
    <header class="site-header">
      <div class="brand"><span class="brand-mark"></span>Bright Voyage</div>
      <nav class="main-nav">
        <a href="#">Home</a>
        <a href="#">Summit Circle</a>
        <a href="#">Book RM</a>
        <a href="#" class="is-current">About</a>
      </nav>
    </header>
    <h1 class="hero-title">MILLIONAIRE <span class="accent">MENTOR</span></h1>
    <p class="hero-intro">Rowan Marsh is CEO and founder to one of the world's fastest growing IT consulting companies in the world, according to Venture Weekly.</p>
    <a href="#" class="btn btn-live">See Rowan Live
      <svg width="22" height="22" viewBox="0 0 24 24" aria-hidden="true"><path d="M3 14l10-8 3 10-6-1-2 5-2-1 1-4z" fill="#fff"/><path d="M18 4l2-2M20 8h3M17 1v2" stroke="#fff" stroke-width="1.6"/></svg>
    </a>
  </section>

  <section class="video-section">
    <p class="mentor-quote">“If you are not chasing your potential<br>you are wasting your life”</p>
    <div class="video-player" role="img" aria-label="Video still of a speaker presenting on stage in front of a projected slide">
      <div class="video-channel"><span class="video-avatar"></span>Talk With Rowan</div>
      <div class="video-actions">
        <div class="video-action">
          <svg width="34" height="34" viewBox="0 0 34 34" aria-hidden="true"><circle cx="17" cy="17" r="15" fill="none" stroke="#fff" stroke-width="2"/><path d="M17 8v9l6 5" fill="none" stroke="#fff" stroke-width="2"/></svg>
          Watch later
        </div>
        <div class="video-action">
          <svg width="38" height="34" viewBox="0 0 38 34" aria-hidden="true"><path d="M22 2l14 13-14 13v-8C12 20 6 23 2 31 3 19 10 11 22 10z" fill="#fff"/></svg>
          Share
        </div>
      </div>
      <div class="video-play">
        <svg width="24" height="24" viewBox="0 0 24 24" aria-hidden="true"><path d="M4 2l18 10L4 22z" fill="#111"/></svg>
      </div>
    </div>
    <a href="#" class="btn btn-cta">Build Your Best Life Now</a>
    <a href="#" class="btn btn-plan">Download Free Business Plan
      <svg width="14" height="14" viewBox="0 0 14 14" aria-hidden="true"><path d="M7 1v8M3 6l4 4 4-4M1 13h12" fill="none" stroke="#fff" stroke-width="2"/></svg>
    </a>
  </section>
</body>
</html>
```